Creation of a construction/bricklaying business website

Following the template format of "Wendmoor 2", the following content would need to be included:
1. Landing page with 3 tiles that go to their own pages.
- Landing page to include background photo and description of services offered.
2. 3 tiles to include:
a) "Contact Us For A Free Quote or Friendly Discussion" Form (middle tile)
b) Case Studies and Testimonials
c) Certifications and Professional Membership
- Design logo to be used from previous PixelHarbor project. Example of logo attached below, please access full JPG files from our account.

Target Market(s)

Prospective clients seeking construction work (bricklaying speciality)

Industry/Entity Type

Residential Construction

Coding

Coded - Design and coding required

Number of Pages Required

4 page

Font styles to use
Sans Serif

Colors

Designer to choose colors to be used in the design.

Requirements
Must have
• Following the template format of "Wendmoor 2", the following content would need to be included:
• 1. Landing parent page with 3 tiles that go to the 3 child pages.
• - Landing page to include background photo and description of services offered.
• 2. 3 tiles to include:
• a) "Contact Us For A Free Quote or Friendly Discussion" Form (middle tile)
• b) Case Studies and Testimonials (first tile / left side)
• c) Certifications and Professional Memberships (third tile / right side) (This should include logos of the relevant organisations being displayed. Specifically QLT and the Keystone Pact QLT).
• - Design logo to be used from previous PixelHarbor project. Example of logo attached below, please access full JPG files from our account.
Nice to have
• Sleek and modern feel.
• Approachable in terms of how people can contact the company for a quote.
• Traditional pictures to give credibility and comfort around choosing this company.
Should not have
• Cheesy pictures
• Over-complicated
• Simple to use
• Easy URL domain name

```html
<!DOCTYPE html>
<html lang="en">
<head>
<meta charset="utf-8">
<title>R.T. Hale Construction Ltd</title>
<link rel="stylesheet" href="https://fonts.googleapis.com/css2?family=Libre+Franklin:wght@300;400;500;600;700&display=swap">
<style>
:root{
  --blue:#0f55a6;
  --blue-dark:#0c4a93;
  --ink:#222831;
  --muted:#a6abb2;
  --light:#f5f5f5;
  --footer:#5e5e5e;
  --teal:#1aa5b8;
  --white:#ffffff;
  --header:rgba(232,236,240,.92);
}
*{margin:0;padding:0;box-sizing:border-box}
html,body{width:1200px;height:3056px;overflow:hidden}
body{font-family:"Libre Franklin",Arial,sans-serif;color:var(--ink);background:var(--white);position:relative}
.abs{position:absolute}

/* header */
.site-header{left:0;top:0;width:1200px;height:130px;background:var(--header);z-index:3}
.brand{left:88px;top:48px;font-weight:700;font-size:38px;color:var(--blue);letter-spacing:-.5px;line-height:1}
.brand small{display:block;font-size:12px;letter-spacing:1.4px;font-weight:600;margin-top:4px}
.brand-square{left:282px;top:32px;width:14px;height:14px;background:var(--blue)}
.contact-strip{top:26px;font-size:17px;font-weight:600;color:var(--blue)}
.contact-strip span{color:var(--ink);font-weight:700}
.quote-btn{left:966px;top:18px;width:144px;height:39px;background:var(--blue);color:#fff;font-size:14px;font-weight:600;display:flex;align-items:center;justify-content:center}
.main-nav{top:84px;left:328px;display:flex;gap:0;font-size:15px;color:var(--ink)}
.main-nav a{color:inherit;text-decoration:none;margin-right:44px}
.main-nav a.active{color:var(--blue)}

/* hero */
.hero{left:0;top:0;width:1200px;height:625px;background:linear-gradient(180deg,#6d86a6 0%,#8b7356 40%,#5e4630 75%,#3d3328 100%)}
.hero-shade{left:0;top:0;width:1200px;height:625px;background:linear-gradient(90deg,rgba(0,0,0,.35),rgba(0,0,0,0) 60%)}
.hero-copy{left:88px;top:272px;width:560px;color:#fff;font-size:34px;font-weight:300;line-height:44px}
.hero-copy b{font-weight:700}
.btn-white{background:#fff;color:var(--blue);font-size:14px;font-weight:600;display:flex;align-items:center;justify-content:center}
.hero-btn{left:88px;top:434px;width:146px;height:39px}
.slide-arrow{width:38px;height:38px;border-radius:50%;background:rgba(255,255,255,.9);left:1074px;display:flex;align-items:center;justify-content:center}
.slide-arrow.ghost{background:rgba(255,255,255,.35)}
.dots{display:flex;gap:8px}
.dots i{display:block;width:13px;height:13px;border-radius:50%;border:2px solid #fff}
.dots i.on{background:#fff}

/* welcome */
.welcome{left:0;top:625px;width:600px;height:455px;background:var(--light)}
.welcome-kicker{left:88px;top:728px;font-size:14px;color:var(--ink)}
.welcome-title{left:88px;top:750px;font-size:28px;color:var(--blue);font-weight:400}
.welcome-title b{font-weight:600}
.welcome-text{left:88px;top:794px;width:425px;font-size:13.5px;line-height:22px;color:var(--muted)}
.btn-blue{background:var(--blue);color:#fff;font-size:14px;font-weight:600;display:flex;align-items:center;justify-content:center;box-shadow:0 6px 14px rgba(15,85,166,.3)}
.welcome-btn{left:88px;top:939px;width:146px;height:38px}
.welcome-photo{left:600px;top:625px;width:600px;height:510px;background:linear-gradient(180deg,#3f7bc9 0%,#8db4e2 45%,#c8c2b6 60%,#a68b70 80%,#8f8c85 100%);z-index:2}
.accent-line{left:587px;top:850px;width:24px;height:3px;background:var(--teal);z-index:3}

/* services */
.services{left:0;top:1080px;width:1200px;height:485px;background:var(--blue)}
.service{width:300px;text-align:center;color:#fff}
.service .icon{width:94px;height:94px;border-radius:50%;border:2px solid #fff;margin:0 auto;display:flex;align-items:center;justify-content:center}
.service .icon.filled{background:#fff}
.service h3{font-size:17px;font-weight:600;margin-top:30px}
.service p{font-size:13.5px;line-height:20px;width:290px;margin:14px auto 0}
.service .more{width:130px;height:39px;margin:20px auto 0;border:1.5px solid #fff;display:flex;align-items:center;justify-content:center;font-size:13.5px;font-weight:500}
.service .more.solid{background:#fff;color:var(--blue)}

/* case studies */
.cases{left:0;top:1565px;width:1200px;height:520px;background:var(--light)}
.section-title{width:1200px;text-align:center;font-size:29px;font-weight:400;color:var(--blue)}
.section-title b{font-weight:600}
.case{width:324px}
.case .photo{width:324px;height:183px}
.case h4{font-size:16px;font-weight:600;line-height:20px;margin-top:26px;width:250px}
.case h4.link{text-decoration:underline}
.case time{display:block;font-size:14px;color:#777;margin-top:18px}
.dots.blue i{border-color:var(--blue);width:13px;height:13px}
.dots.blue i.on{background:var(--blue)}

/* certifications */
.badge{width:159px;height:110px;background:#fff;border:1px solid #e4e4e4;box-shadow:0 2px 8px rgba(0,0,0,.06);display:flex;align-items:center;justify-content:center}
.badge .mark{width:106px;height:62px;background:#3a3a3a;border-radius:3px}
.badge .mark.grey{background:#6a6a6a}
.badge .mark.red{background:#c4112f}
.cert-arrow{font-size:20px;color:var(--blue)}
.cert-arrow.dim{color:#bbb}

/* quote band */
.quote-band{left:0;top:2414px;width:1200px;height:132px;background:var(--blue);color:#fff}
.quote-title{left:175px;top:2447px;font-size:22px;font-weight:400}
.quote-title b{font-weight:700}
.quote-sub{left:175px;top:2492px;font-size:13.5px}
.quote-cta{left:858px;top:2459px;width:165px;height:38px;background:#fff;color:var(--blue);font-size:13.5px;font-weight:600;display:flex;align-items:center;justify-content:center}

/* footer */
.site-footer{left:0;top:2546px;width:1200px;height:510px;background:var(--footer);color:#fff}
.footer-title{top:2632px;width:1200px;text-align:center;font-size:27px;font-weight:400}
.footer-brand{left:88px;top:2732px;font-size:32px;font-weight:700;line-height:1}
.footer-brand small{display:block;font-size:10px;letter-spacing:1.2px;margin-top:3px}
.footer-legal{left:88px;top:2800px;font-size:12.5px;line-height:22px}
.divider{width:1px;height:183px;background:rgba(255,255,255,.35);top:2689px}
.footer-label{font-size:13.5px;font-weight:600}
.footer-call{left:438px;top:2755px;font-size:22px;font-weight:300}
.footer-info{left:438px;top:2786px;font-size:13px;line-height:20px}
.social{display:flex;gap:13px;left:789px;top:2756px}
.social i{display:block;width:36px;height:36px;border-radius:50%;background:#4a4a4a;border:1px solid #777}
.social i.on{background:var(--blue);border-color:var(--blue)}
.footer-nav{top:2914px;left:0;width:1200px;display:flex;justify-content:center;font-size:14px}
.footer-nav a{color:#fff;text-decoration:none;margin:0 23px}
.footer-rule{left:80px;top:2956px;width:1040px;height:1px;background:rgba(255,255,255,.2)}
.footer-policy{top:3003px;width:1200px;text-align:center;font-size:13px}
</style>
</head>
<body>

<!-- hero -->
<div class="abs hero" role="img" aria-label="Photo of a timber-framed house under construction"></div>
<div class="abs hero-shade"></div>

<header class="abs site-header">
  <div class="abs brand">R.T.Hale<small>CONSTRUCTION LTD</small></div>
  <div class="abs brand-square"></div>
  <div class="abs contact-strip" style="left:491px">Call Us: <svg width="18" height="18" viewBox="0 0 24 24" style="vertical-align:-3px"><circle cx="12" cy="12" r="10.5" fill="none" stroke="#0f55a6" stroke-width="2"/><path d="M8.5 7l2 2-1 1.5a7 7 0 0 0 4 4l1.5-1 2 2-1.5 1.5C11 16.5 7.5 13 7 8.5z" fill="#0f55a6"/></svg> <span>07700900431</span></div>
  <div class="abs contact-strip" style="left:748px;font-size:15px;top:28px">Email: <span style="font-weight:400">info@rthale.co.uk</span></div>
  <div class="abs quote-btn">Get a Quote</div>
  <nav class="abs main-nav">
    <a class="active" href="#">-- Home --</a><a href="#">About Us</a><a href="#">Services</a><a href="#">Case Studies</a><a href="#">Testimonials</a><a href="#">Certifications</a><a href="#" style="margin-right:0">Contact Us</a>
  </nav>
</header>

<p class="abs hero-copy">We believe in <b>full transparency</b> and this is reflected in the <b>jobs we quote for you.</b></p>
<div class="abs btn-white hero-btn">Explore More</div>
<div class="abs slide-arrow ghost" style="top:333px"><svg width="12" height="12" viewBox="0 0 12 12"><path d="M8 2L4 6l4 4" fill="none" stroke="#fff" stroke-width="1.6"/></svg></div>
<div class="abs slide-arrow" style="top:382px"><svg width="12" height="12" viewBox="0 0 12 12"><path d="M4 2l4 4-4 4" fill="none" stroke="#333" stroke-width="1.6"/></svg></div>
<div class="abs dots" style="left:572px;top:568px"><i></i><i class="on"></i><i></i></div>

<!-- welcome -->
<section class="abs welcome"></section>
<p class="abs welcome-kicker">Welcome to</p>
<h1 class="abs welcome-title">R. T. <b>Hale Construction Ltd</b></h1>
<p class="abs welcome-text">We pride ourselves on attention to detail, pride in our completed project and client satisfaction. We believe in full transparency and this is reflected in the jobs we quote for you. We break down each step with both labour and materials cost so you can see exactly what you are paying for.</p>
<div class="abs btn-blue welcome-btn">Explore More</div>
<div class="abs welcome-photo" role="img" aria-label="Photo of a modern two-storey house with timber cladding nearing completion"></div>
<div class="abs accent-line"></div>

<!-- services -->
<section class="abs services"></section>
<div class="abs service" style="left:98px;top:1208px">
  <div class="icon"><svg width="46" height="46" viewBox="0 0 46 46" fill="none" stroke="#fff" stroke-width="2"><rect x="6" y="6" width="16" height="16"/><rect x="22" y="22" width="18" height="18"/><path d="M22 14h8v8M14 22v8h8"/></svg></div>
  <h3>Extensions</h3>
  <p>Contrary to popular belief, Lorem Ipsum is not simply random text. It has roots in a piece of classical Latin ...</p>
  <div class="more">Read More</div>
</div>
<div class="abs service" style="left:449px;top:1208px">
  <div class="icon filled"><svg width="46" height="46" viewBox="0 0 46 46" fill="none" stroke="#0f55a6" stroke-width="2"><rect x="8" y="8" width="30" height="30"/><path d="M15 24l8-7 8 7v8H15z"/><rect x="21" y="26" width="4" height="6"/></svg></div>
  <h3>New Build / New Houses</h3>
  <p>Contrary to popular belief, Lorem Ipsum is not simply random text. It has roots in a piece of classical Latin ...</p>
  <div class="more solid">Read More</div>
</div>
<div class="abs service" style="left:801px;top:1208px">
  <div class="icon"><svg width="46" height="46" viewBox="0 0 46 46" fill="none" stroke="#fff" stroke-width="2"><circle cx="23" cy="23" r="17"/><path d="M7 16h32M6 23h34M7 30h32M18 9v7M28 9v7M13 16v7M23 16v7M33 16v7M18 23v7M28 23v7M23 30v7"/></svg></div>
  <h3>Garden Walls</h3>
  <p>Contrary to popular belief, Lorem Ipsum is not simply random text. It has roots in a piece of classical Latin ...</p>
  <div class="more">Read More</div>
</div>

<!-- case studies -->
<section class="abs cases"></section>
<h2 class="abs section-title" style="top:1630px">Case <b>Studies</b></h2>
<article class="abs case" style="left:88px;top:1691px">
  <div class="photo" role="img" aria-label="Photo of a retaining boundary wall in brick" style="background:linear-gradient(180deg,#9fb3c9 0%,#b88a62 45%,#8b6a48 100%)"></div>
  <h4>Built retaining boundary wall in ealing.</h4>
  <time>24/05/2018</time>
</article>
<article class="abs case" style="left:438px;top:1691px">
  <div class="photo" role="img" aria-label="Photo of a stone-capped parapet wall" style="background:linear-gradient(180deg,#3f5a2e 0%,#bfb49a 40%,#2a2a2a 75%,#1e1e1e 100%)"></div>
  <h4 class="link">Built parapet wall in chiswick</h4>
  <time>09/07/2018</time>
</article>
<article class="abs case" style="left:788px;top:1691px">
  <div class="photo" role="img" aria-label="Photo of a new red brick garden wall" style="background:linear-gradient(180deg,#c8d2dc 0%,#b56a58 35%,#a05a4a 60%,#6b6a4a 100%)"></div>
  <h4>Built new brick wall in ealing, london</h4>
  <time>01/03/2018</time>
</article>
<div class="abs dots blue" style="left:576px;top:1995px"><i class="on"></i><i></i><i></i></div>

<!-- certifications -->
<h2 class="abs section-title" style="top:2151px">Certifications &amp; <b>Memberships</b></h2>
<div class="abs cert-arrow dim" style="left:138px;top:2268px">&#8249;</div>
<div class="abs badge" style="left:175px;top:2226px" role="img" aria-label="Membership badge"><div class="mark"></div></div>
<div class="abs badge" style="left:347px;top:2226px" role="img" aria-label="Keystone Pact QLT badge"><div class="mark grey"></div></div>
<div class="abs badge" style="left:520px;top:2226px" role="img" aria-label="Building approval badge"><div class="mark grey" style="background:#8a8a8a"></div></div>
<div class="abs badge" style="left:693px;top:2226px" role="img" aria-label="Membership badge"><div class="mark red"></div></div>
<div class="abs badge" style="left:866px;top:2226px" role="img" aria-label="Building approval badge"><div class="mark grey" style="background:#8a8a8a"></div></div>
<div class="abs cert-arrow" style="left:1050px;top:2268px">&#8250;</div>

<!-- quote band -->
<section class="abs quote-band"></section>
<h3 class="abs quote-title" style="color:#fff">Get A <b>Free Quote</b></h3>
<p class="abs quote-sub" style="color:#fff">Feel free to get in touch and we can talk through what you are looking to achieve ...</p>
<div class="abs quote-cta">Get A Quote Now!</div>

<!-- footer -->
<footer class="abs site-footer"></footer>
<h2 class="abs footer-title" style="color:#fff">Get <span style="font-weight:400">In Touch</span></h2>
<div class="abs footer-brand" style="color:#fff">R.T.Hale<small>CONSTRUCTION LTD</small></div>
<p class="abs footer-legal" style="color:#fff">© 2018 R. T. Hale Construction Ltd.<br>All Right Reserved.</p>
<div class="abs divider" style="left:383px"></div>
<div class="abs divider" style="left:733px"></div>
<p class="abs footer-label" style="left:438px;top:2719px;color:#fff">Need Help? Contact Us</p>
<p class="abs footer-call" style="color:#fff">Call: 07700900431</p>
<p class="abs footer-info" style="color:#fff">E: info@rthale.co.uk<br><br>48 Elm Quarry Road,<br>Brookfield, BK4 2LT</p>
<p class="abs footer-label" style="left:789px;top:2719px;color:#fff">Get Social:</p>
<div class="abs social" aria-label="Social links"><i></i><i class="on"></i><i></i><i></i></div>
<svg class="abs" style="left:1066px;top:2722px" width="32" height="36" viewBox="0 0 32 36" fill="none" stroke="#fff" stroke-width="2"><path d="M16 30V6M8 14l8-8 8 8M2 34h28"/></svg>
<nav class="abs footer-nav">
  <a href="#">-- Home --</a><a href="#">About Us</a><a href="#">Services</a><a href="#">Case Studies</a><a href="#">Testimonials</a><a href="#">Certifications</a><a href="#">Contact Us</a>
</nav>
<div class="abs footer-rule"></div>
<p class="abs footer-policy" style="color:#fff">Privacy Policy | Legal</p>

</body>
</html>
```